Australian Meat, Seafood and Fresh Produce Website

Our organization is looking to design a simple, but eye catching website to show our services.
Our company exports West Australian FRESH fruit and vegetables, seafood and meat.
The website we are looking for would consist of:
- Landing Page
- Company info
- Directors bio
- Page that highlights our products
- Contact us page
We would like it to have a Chinese translated version as well.
Tobin
Target Market(s)
Chinese Market
Industry/Entity Type
It Company
Number of Pages Required
1 page
Look and feel
Each slider illustrates characteristics of the customer's brand and the style your logo design should communicate.

```html
<!DOCTYPE html>
<html lang="en">
<head>
<meta charset="utf-8">
<title>Swanbrook Produce</title>
<link href="https://fonts.googleapis.com/css2?family=Oswald:wght@400;500&family=Open+Sans:wght@400;600;700&display=swap" rel="stylesheet">
<style>
:root{
  --red:#c8171b;
  --dark-red:#a51014;
  --ink:#222;
  --muted:#666;
  --light:#f4f4f4;
  --charcoal:#2b2b2b;
  --footer:#1e1e1e;
  --white:#fff;
}
*{box-sizing:border-box;margin:0;padding:0}
html,body{width:741px;height:1200px;overflow:hidden;background:var(--white)}
body{font-family:"Open Sans",Arial,sans-serif;color:var(--ink);font-size:8px;position:relative}
.site-header{height:68px;display:flex;align-items:center;justify-content:space-between;padding:0 30px;background:var(--white)}
.brand{font-family:"Open Sans",Arial,sans-serif;font-weight:700;font-size:17px;color:var(--ink)}
.main-nav{display:flex;align-items:center;gap:20px;font-size:8px;font-weight:600;color:#444}
.main-nav .active{color:var(--red)}
.lang{background:var(--charcoal);color:var(--white);padding:4px 8px;display:flex;align-items:center;gap:4px}
.hero{position:relative;height:342px;background:linear-gradient(180deg,#8a3a2e 0%,#c27a66 35%,#d9a08d 60%,#7a3a30 100%)}
.hero-text{position:absolute;left:48px;top:140px;color:var(--white);font-family:"Oswald",Arial,sans-serif}
.hero-text h1{font-weight:500;font-size:24px;letter-spacing:.5px;text-transform:uppercase}
.hero-text h2{font-weight:400;font-size:26px;margin-top:2px}
.btn{display:inline-block;margin-top:16px;background:var(--charcoal);color:var(--white);font-family:"Open Sans",Arial,sans-serif;font-size:9px;font-weight:600;padding:8px 16px}
.slider-dots{position:absolute;right:22px;top:140px;display:flex;flex-direction:column;gap:7px}
.slider-dots span{width:6px;height:6px;border-radius:50%;background:var(--white);opacity:.7}
.welcome{height:160px;text-align:center;padding:26px 70px 0}
.section-title{font-family:"Oswald",Arial,sans-serif;font-weight:500;font-size:17px;text-transform:uppercase}
.section-title .accent{color:var(--red)}
.rule{width:40px;height:2px;background:var(--red);margin:6px auto 12px}
.welcome p{font-size:7.5px;line-height:1.75;color:var(--muted)}
.products{height:270px;background:linear-gradient(180deg,#3a3a3a,#262626);padding-top:20px;text-align:center}
.products .section-title{color:var(--white)}
.cards{display:flex;justify-content:center;gap:7px;margin-top:4px}
.card{width:148px;background:var(--white)}
.card .photo{height:98px}
.card h3{font-family:"Oswald",Arial,sans-serif;font-weight:500;font-size:11px;color:var(--red);margin-top:9px}
.card p{font-size:6.5px;color:var(--muted);line-height:1.6;padding:4px 12px 12px}
.news-blog{display:flex;height:212px;padding:24px 48px 0}
.news{width:150px}
.blog{flex:1;padding-left:10px}
.block-title{font-family:"Oswald",Arial,sans-serif;font-weight:500;font-size:14px;text-transform:uppercase;margin-bottom:12px}
.block-title .accent{color:var(--red)}
.news-item{display:flex;gap:8px;margin-bottom:14px}
.date{width:26px;height:30px;border:1px solid #ccc;text-align:center;font-weight:700;font-size:10px;line-height:18px}
.date small{display:block;font-size:5px;line-height:8px;color:var(--muted);font-weight:400}
.news-item h4{font-size:7px;color:var(--red);font-weight:700}
.news-item p{font-size:6.5px;color:var(--muted);margin-top:2px}
.posts{display:flex;gap:10px}
.post{width:145px;box-shadow:0 1px 3px rgba(0,0,0,.25)}
.post .photo{height:70px}
.post span{display:block;font-size:6.5px;font-weight:700;text-align:center;padding:6px 0}
.locations{height:58px;background:var(--red);display:flex;align-items:center;padding:0 48px;color:var(--white)}
.locations h3{font-family:"Oswald",Arial,sans-serif;font-weight:400;font-size:16px;text-transform:uppercase;width:122px}
.select{width:172px;height:22px;background:var(--white);color:#555;font-size:7px;display:flex;align-items:center;justify-content:space-between;padding:0 8px}
.contact{margin-left:52px;font-size:9px;line-height:1.6}
.contact strong{font-family:"Oswald",Arial,sans-serif;font-weight:400;font-size:13px;display:block}
.phone{margin-left:auto;display:flex;align-items:center;gap:8px;font-family:"Oswald",Arial,sans-serif;font-size:20px}
.site-footer{height:90px;background:var(--footer);color:#bbb;display:flex;justify-content:space-between;align-items:center;padding:0 48px}
.site-footer p{font-size:6.5px;line-height:2}
.follow{font-size:7px;font-weight:700;color:var(--white)}
.socials{display:flex;gap:4px;margin-top:5px}
.socials span{width:13px;height:13px;background:#555}
</style>
</head>
<body>
<header class="site-header">
  <div class="brand">Swanbrook Produce</div>
  <nav class="main-nav">
    <span class="active">HOME</span><span>ABOUT US</span><span>BIO</span><span>PRODUCTS</span><span>CONTACT US</span>
    <span class="lang">English
      <svg width="7" height="5" viewBox="0 0 7 5"><path d="M0 0h7L3.5 5z" fill="#fff"/></svg>
    </span>
  </nav>
</header>

<section class="hero" role="img" aria-label="Butcher's display of whole meat carcasses hanging in a cool room">
  <div class="hero-text">
    <h1>Exports West Australian</h1>
    <h2>Fresh fruit and vegetables, seafood and meat</h2>
    <span class="btn">VIEW MORE</span>
  </div>
  <div class="slider-dots"><span></span><span></span><span></span></div>
</section>

<section class="welcome">
  <h2 class="section-title">Welcome to <span class="accent">Swanbrook Produce</span></h2>
  <div class="rule"></div>
  <p>Swanbrook Produce (SBP) aims to supply high quality West Australian produce to the rest of the world. Western Australia is known for its high quality farming practices and environment, which produces fresh seafood, fruit and vegetables of a calibre that is respected globally. With a management team and first class suppliers, our organisation provides quality ingredients straight from farm or ocean to purchaser. This document aims to outline both our management team and their backgrounds, as well as the suppliers who will initially supply our global customers.</p>
</section>

<section class="products">
  <h2 class="section-title">Our Company Exports West Australian</h2>
  <div class="rule"></div>
  <div class="cards">
    <div class="card"><div class="photo" role="img" aria-label="Assorted fresh fruit" style="background:linear-gradient(135deg,#d9412b,#f0a030,#6a9a2a)"></div><h3>FRESH FRUIT</h3><p>Lorem ipsum is simply dummy text of the printing and typesetting industry</p></div>
    <div class="card"><div class="photo" role="img" aria-label="Fresh vegetables" style="background:linear-gradient(135deg,#c8261c,#e8b020,#3f8a2a)"></div><h3>VEGETABLES</h3><p>Lorem ipsum is simply dummy text of the printing and typesetting industry</p></div>
    <div class="card"><div class="photo" role="img" aria-label="Fresh fish on ice" style="background:linear-gradient(135deg,#9fb3c2,#dfe6ea,#6f8796)"></div><h3>SEAFOOD</h3><p>Lorem ipsum is simply dummy text of the printing and typesetting industry</p></div>
    <div class="card"><div class="photo" role="img" aria-label="Cuts of raw red meat" style="background:linear-gradient(135deg,#9a2525,#d0605a,#7a1a1a)"></div><h3>MEAT</h3><p>Lorem ipsum is simply dummy text of the printing and typesetting industry</p></div>
  </div>
</section>

<section class="news-blog">
  <div class="news">
    <h2 class="block-title">Latest <span class="accent">News</span></h2>
    <div class="news-item"><div class="date">20<small>MAY</small></div><div><h4>NEWS HEADLINE HERE</h4><p>Lorem ipsum dolor sit amet, con</p></div></div>
    <div class="news-item"><div class="date">20<small>MAY</small></div><div><h4>NEWS HEADLINE HERE</h4><p>Lorem ipsum dolor sit amet, con</p></div></div>
  </div>
  <div class="blog">
    <h2 class="block-title">Blog</h2>
    <div class="posts">
      <div class="post"><div class="photo" role="img" aria-label="Market stall of fresh produce" style="background:linear-gradient(135deg,#b84a2a,#e0a040,#5a8a30)"></div><span>SUPPLIERS</span></div>
      <div class="post"><div class="photo" role="img" aria-label="Fresh fish at a seafood market" style="background:linear-gradient(135deg,#6f8796,#c9d3d9,#4a5a66)"></div><span>SUSTAINABLE SEAFOOD</span></div>
      <div class="post"><div class="photo" role="img" aria-label="Premium beef cuts" style="background:linear-gradient(135deg,#7a1a1a,#c04a40,#5a1414)"></div><span>GOLD AWARD</span></div>
    </div>
  </div>
</section>

<section class="locations">
  <h3>Locations</h3>
  <div class="select">Select Location
    <svg width="8" height="5" viewBox="0 0 8 5"><path d="M0 0h8L4 5z" fill="#333"/></svg>
  </div>
  <div class="contact"><strong>SWANBROOK PRODUCE</strong>Email: info@swanbrook.example</div>
  <div class="phone">
    <svg width="16" height="16" viewBox="0 0 24 24"><path d="M6.6 10.8a15 15 0 0 0 6.6 6.6l2.2-2.2a1 1 0 0 1 1-.25 11.4 11.4 0 0 0 3.6.57 1 1 0 0 1 1 1V20a1 1 0 0 1-1 1A17 17 0 0 1 3 4a1 1 0 0 1 1-1h3.5a1 1 0 0 1 1 1c0 1.25.2 2.45.57 3.57a1 1 0 0 1-.25 1z" fill="#fff"/></svg>
    612 555 0148
  </div>
</section>

<footer class="site-footer">
  <div><p>Privacy Policy | Terms Conditions | Sitemap | Contact Us</p><p>Copyright © 2015 . All Rights Reserved</p></div>
  <div><div class="follow">FOLLOW US</div><div class="socials"><span></span><span></span><span></span><span></span><span></span></div></div>
</footer>
</body>
</html>
```